My name is Tomas Berenji, and I have done business with your company several times. I need a business card to represent my business, I own a company by the name of VELMINO Suntan Lotion & Sunscreen.
My requirements are as follow: My company logo in the brightest gold possible, on a black, grainy (sandy) background, with shading around the each element. With the company name in gold, a stylized coconut trees, and some type of wave graphic in gold. "A product of the USA, Harwick Cove, NY"
"For comments, suggestion, or ordering please contact us at:
velmino42@brisalto.com"

"VELMINO™ Tanning Lotion & Sunscreen―Crafted with Care"

Velmino Tanning Lotion & Sunscreen is the most extraordinary and innovative sun tanning product to emerge in several generations. The constituents of this product are formidable substances that protect the skin against the aftermath of sun exposure−before you exposed yourself to the sun’s rays. The Aloe Vera in this product, along with other oils and cream, are specifically manufactured to lessen the symptoms of extended exposure to the sun. Velmino is designed to provide a Broad Spectrum Protection (50) that assist in the reduction of (UVA) and (UVB) radiation to create a magnificent sun-absorbing, long-lasting, deep dark bronzing experience.
Thank you,
Tomas Berenji
tomasbberenji@nexipost.com

Target Market(s)

Sunscreen

Industry/Entity Type

Business

Contact Information for Business Card

VELMINO™ Tanning Lotion and Sunscreen
Crafted with Care

Velmino Tanning Lotion is the most extraordinary and innovative sun tanning product to emerge in several generations. The constituents of this product are formidable substances that protect the skin against the aftermath of sun exposure−before you exposed yourself to the sun’s rays. The Aloe Vera, in this product, along with other oils and cream, are specifically manufactured to lessen the symptoms of extended exposure to the sun. Velmino protects your skin from dehydration and treat your skin with the products we apply to ourselves after a sunburn−before the sun tanning process begins. Velmino is designed to provide a Broad Spectrum Protection (50) that assist in the reduction of (UVA) and (UVB) radiation to create a magnificent sun-absorbing, long-lasting, deep dark bronzing experience.

Colors
fece3e
acd136

Requirements
Must have
• Black Card Stock with grainy surface, Gold Logo, stylized Coconut Palm Tree, Company Name, email address, and NYC location.
• Modern Layout with Modern fonts and graphics

```html
<!DOCTYPE html>
<html lang="en">
<head>
<meta charset="utf-8">
<title>Velmino Business Card</title>
<link rel="stylesheet" href="https://fonts.googleapis.com/css2?family=Marcellus&family=Open+Sans:wght@400;600;700&family=Roboto+Slab:wght@700&display=swap">
<style>
  :root {
    --backdrop: #8f8f8f;
    --card-black: #141414;
    --gold: #c9a06a;
    --gold-bright: #e3b94d;
    --gold-rule: #b8802e;
    --rule-light: #8a8a80;
    --text-grey: #b9b9b9;
    --white: #ffffff;
    --palm-deep: #1f5a1c;
    --palm-mid: #3f8f2c;
    --palm-light: #7cc24a;
  }
  html, body {
    margin: 0;
    padding: 0;
    width: 1105px;
    height: 1200px;
    overflow: hidden;
    background: var(--backdrop);
  }
  .sheet {
    position: relative;
    width: 1105px;
    height: 1200px;
  }
  .card {
    position: absolute;
    left: 196px;
    width: 720px;
    height: 413px;
    background:
      radial-gradient(circle at 30% 40%, rgba(255,255,255,0.035), transparent 60%),
      var(--card-black);
    box-shadow: 2px 4px 10px rgba(0,0,0,0.45);
    overflow: hidden;
    font-family: "Open Sans", Arial, sans-serif;
  }
  .card--front { top: 145px; }
  .card--back { top: 602px; }

  .palm-fronds {
    position: absolute;
    right: 0;
    top: 0;
    width: 320px;
    height: 350px;
  }

  .brand-mark {
    position: absolute;
    border-radius: 50%;
    background: radial-gradient(circle at 40% 35%, #f2cf6a, #c08a22 70%, #7a5012);
  }
  .card--front .brand-mark { left: 109px; top: 111px; width: 102px; height: 102px; }
  .card--back .brand-mark { left: 145px; top: 132px; width: 102px; height: 102px; }

  .front-name {
    position: absolute;
    left: 50px;
    top: 212px;
    margin: 0;
    font-family: "Marcellus", Georgia, serif;
    font-weight: 400;
    font-size: 46px;
    letter-spacing: 1px;
    color: var(--gold);
    line-height: 1;
  }
  .front-subtitle {
    position: absolute;
    left: 83px;
    top: 262px;
    margin: 0;
    font-size: 19px;
    color: var(--gold);
    letter-spacing: 0.5px;
    line-height: 1;
  }
  .front-rule {
    position: absolute;
    left: 46px;
    top: 300px;
    width: 628px;
    height: 1px;
    background: var(--rule-light);
  }
  .person {
    position: absolute;
    left: 46px;
    top: 312px;
    margin: 0;
    line-height: 1;
  }
  .person-name {
    font-size: 24px;
    font-weight: 700;
    color: var(--gold);
  }
  .person-role {
    font-size: 19px;
    font-weight: 600;
    color: var(--gold-bright);
  }
  .contact-line {
    position: absolute;
    left: 46px;
    top: 350px;
    margin: 0;
    font-size: 17.5px;
    color: var(--text-grey);
    white-space: nowrap;
    line-height: 1;
  }
  .contact-label {
    font-weight: 700;
    color: var(--gold);
  }

  .back-name {
    position: absolute;
    left: 262px;
    top: 134px;
    margin: 0;
    font-family: "Marcellus", Georgia, serif;
    font-weight: 400;
    font-size: 52px;
    color: var(--white);
    letter-spacing: 1px;
    line-height: 1;
  }
  .back-name sup {
    font-family: "Open Sans", Arial, sans-serif;
    font-size: 15px;
    vertical-align: top;
    position: relative;
    top: 2px;
  }
  .back-rule {
    position: absolute;
    left: 262px;
    top: 196px;
    width: 288px;
    height: 3px;
    background: var(--gold-rule);
  }
  .back-tagline {
    position: absolute;
    left: 262px;
    top: 204px;
    margin: 0;
    font-family: "Roboto Slab", Georgia, serif;
    font-weight: 700;
    font-size: 19px;
    color: var(--white);
    letter-spacing: -0.3px;
    line-height: 1;
    white-space: nowrap;
  }
  .back-info {
    position: absolute;
    left: 0;
    right: 0;
    top: 296px;
    margin: 0;
    text-align: center;
    font-size: 18px;
    line-height: 26px;
    color: var(--white);
  }
  .back-email {
    font-weight: 700;
    font-size: 20px;
  }
</style>
</head>
<body>
<main class="sheet">
  <section class="card card--front">
    <svg class="palm-fronds" viewBox="0 0 320 350" role="img" aria-label="Illustration of green coconut palm fronds hanging into the top-right corner">
      <defs>
        <radialGradient id="palmShade" cx="80%" cy="15%" r="85%">
          <stop offset="0%" stop-color="#7cc24a"/>
          <stop offset="45%" stop-color="#3f8f2c"/>
          <stop offset="100%" stop-color="#1f5a1c" stop-opacity="0"/>
        </radialGradient>
      </defs>
      <path d="M10 0 H320 V260 C300 300 260 330 215 350 C200 300 160 240 110 190 C70 150 30 80 10 0 Z" fill="url(#palmShade)"/>
    </svg>

    <div class="brand-mark"></div>
    <h1 class="front-name">VELMINO</h1>
    <p class="front-subtitle">SUNTAN LOTION</p>
    <div class="front-rule"></div>
    <p class="person"><span class="person-name">TOMAS BERENJI</span><span class="person-name"> &nbsp;-&nbsp; </span><span class="person-role">CEO/Founder</span></p>
    <p class="contact-line"><span class="contact-label">Phone:</span> 555 214 7093&nbsp; <span class="contact-label">Mobile:</span> 555 308 6417&nbsp; <span class="contact-label">Web:</span> www.velminosun.com</p>
  </section>

  <section class="card card--back">
    <div class="brand-mark"></div>
    <h2 class="back-name">VELMINO<sup>TM</sup></h2>
    <div class="back-rule"></div>
    <p class="back-tagline">Tanning Lotion-Crafted with Care</p>
    <p class="back-info">A product of the USA, Harwick Cove, NY<br>For comments, suggestion, or ordering please contact us at:<br><span class="back-email">velmino42@brisalto.com</span></p>
  </section>
</main>
</body>
</html>
```